Thank You Card design for a federal credit union

I am looking to have a thank you card designed.
Specs:
Flat size of 9.5"x6.5" folds to final size of 4.75"x6.5", it will print full color on the front and back. Below, you will see their logo, which needs to print on the inside of the folded card. I also attached images of their current card. They would like to keep the blue color but are open to design on the front. This is a Federal Credit Union, so please make the design, modern and professional. Below is the text that needs to print below the logo on the inside of the card. The text and logo will print below the fold on the inside, leave the top portion (above the panel) white.
Inside text:
Our Members are the foundation of our Credit Union. We sincerely thank you for your loyalty, your business and the opportunity to serve you.
Target Market(s)
Clients of a federal credit union
Industry/Entity Type
Union
Requirements
Must have
- a simple, professional, and modern feel. "Thank You for your business" must be on the front section in some variation.
Should not have
- nothing flashy or too many colors. keep it simple

```html
<!DOCTYPE html>
<html lang="en">
<head>
<meta charset="utf-8">
<title>Thank You Card – Front</title>
<link rel="stylesheet" href="https://fonts.googleapis.com/css2?family=Michroma&family=Allura&display=swap">
<style>
  :root {
    --page-bg: #e6e6e8;
    --card-navy: #1b2470;
    --card-mid: #1d3f9a;
    --card-glow: #1a6fb4;
    --ink-white: #ffffff;
    --ink-shadow: rgba(5, 10, 45, 0.75);
  }
  html, body {
    margin: 0;
    padding: 0;
    width: 1200px;
    height: 1198px;
    overflow: hidden;
    background: var(--page-bg);
  }
  .stage {
    position: relative;
    width: 1200px;
    height: 1198px;
    display: flex;
    align-items: center;
    justify-content: center;
  }
  .card-front {
    position: relative;
    width: 1000px;
    height: 730px;
    background: radial-gradient(ellipse 55% 60% at 50% 48%,
                var(--card-glow) 0%,
                var(--card-mid) 45%,
                var(--card-navy) 100%);
    box-shadow: 0 8px 24px rgba(0, 0, 0, 0.18);
    color: var(--ink-white);
  }
  .lead-in {
    position: absolute;
    left: 100px;
    top: 240px;
    margin: 0;
    font-family: "Michroma", sans-serif;
    font-size: 33px;
    letter-spacing: 1px;
    font-weight: 400;
    text-shadow: 2px 2px 2px var(--ink-shadow);
  }
  .headline {
    position: absolute;
    left: 240px;
    top: 300px;
    margin: 0;
    font-family: "Allura", cursive;
    font-weight: 400;
    font-size: 150px;
    line-height: 1;
    letter-spacing: 6px;
    text-shadow: 2px 3px 3px var(--ink-shadow);
  }
  .sign-off {
    position: absolute;
    right: 80px;
    top: 410px;
    margin: 0;
    font-family: "Michroma", sans-serif;
    font-size: 26px;
    line-height: 1.25;
    letter-spacing: 1px;
    text-align: right;
    text-shadow: 2px 2px 2px var(--ink-shadow);
  }
</style>
</head>
<body>
  <main class="stage">
    <section class="card-front" aria-label="Thank you card front">
      <p class="lead-in">WE WOULD LIKE TO SAY</p>
      <h1 class="headline">thanks you...</h1>
      <p class="sign-off">STAY<br>WITH US</p>
    </section>
  </main>
</body>
</html>
```